"Show Times" Poster for Stunt Show

I need a fairly simple 24"x 36" poster made. I'm a professional mountain bike stunt rider and I need a poster to put on a sandwich board to display my showtimes for people walking by. The top of the poster will say: Mountain Bike (Trials) Stunt Show This text will be centered at the top BUT I want the "(Trials)" to be slightly crooked and a bit opaque with a stamped-looking font and overlap the other words just slightly. Hopefully that makes sense. Somewhere in the middle will be a photoshopped picture of me doing a stunt on my bike. The bottom will have a blank white space titled, "Show Times:" that I can write my showtimes inside of. I've attached a wildly crude and poor drawing of the basic concept. Remember, this is for a stunt show so it must look cool and have some rad colors and design... but also be simple. I will provide a picture of myself riding to be used in the poster. It will take up the middle third.

Target Market(s)

Families, Parents, Kids, general public, mountain bike enthusiastss

Industry/Entity Type

Entertainment Industry

Font styles to use
Sans Serif

Colors

Designer to choose colors to be used in the design.

Requirements
Must have
• A blank, rectangular, white space on the bottom for Show times Labelled "Show Times:"
Nice to have
• I'd like background of the whole poster to be relatively black with cool subtle graphics.

```html
<!DOCTYPE html>
<html lang="en">
<head>
<meta charset="utf-8">
<title>Mountain Bike Trials Stunt Show – Show Times</title>
<link rel="stylesheet" href="https://fonts.googleapis.com/css2?family=Montserrat:ital,wght@0,800;1,800&family=Oswald:wght@700&display=swap">
<style>
  :root {
    --ink: #150606;
    --blood: #b3120f;
    --deep-red: #5c0707;
    --stamp-red: #e8140f;
    --night-blue: #141a6b;
    --royal-blue: #1d2fb0;
    --cyan: #1ee6ea;
    --white: #ffffff;
    --photo-dark: #3a3a3e;
    --photo-mid: #7b7d82;
  }
  * { margin: 0; padding: 0; box-sizing: border-box; }
  html, body { width: 938px; height: 1200px; overflow: hidden; background: var(--ink); }
  .poster {
    position: relative;
    width: 938px;
    height: 1200px;
    overflow: hidden;
    font-family: "Montserrat", sans-serif;
  }
  .poster__backdrop {
    position: absolute;
    inset: 0;
    background:
      radial-gradient(ellipse 420px 300px at 160px 180px, rgba(179,18,15,0.65), transparent 70%),
      radial-gradient(ellipse 360px 260px at 760px 90px, rgba(140,14,12,0.5), transparent 70%),
      radial-gradient(ellipse 520px 360px at 820px 620px, rgba(29,47,176,0.75), transparent 70%),
      radial-gradient(ellipse 420px 320px at 80px 760px, rgba(29,47,176,0.7), transparent 70%),
      radial-gradient(ellipse 520px 300px at 820px 1050px, rgba(179,18,15,0.8), transparent 70%),
      linear-gradient(180deg, #1a0606 0%, #140a2a 55%, #2a0812 100%);
  }
  .headline {
    position: absolute;
    left: 0;
    right: 0;
    top: 0;
    text-align: center;
  }
  .headline__discipline {
    position: absolute;
    left: 0; right: 0;
    top: 36px;
    padding-left: 8px;
    font-size: 62px;
    font-weight: 800;
    color: var(--cyan);
    letter-spacing: 0.5px;
    line-height: 1;
  }
  .headline__trials {
    position: absolute;
    left: 0; right: 0;
    top: 84px;
    font-family: "Oswald", sans-serif;
    font-weight: 700;
    font-size: 122px;
    line-height: 1;
    color: var(--stamp-red);
    opacity: 0.88;
    transform: rotate(-3deg);
    letter-spacing: 2px;
    padding-left: 10px;
  }
  .headline__show {
    position: absolute;
    left: 0; right: 0;
    top: 200px;
    font-size: 91px;
    font-weight: 800;
    color: var(--white);
    line-height: 1;
    padding-left: 30px;
    letter-spacing: 1px;
  }
  .rider-photo {
    position: absolute;
    left: 175px;
    top: 306px;
    width: 630px;
    height: 620px;
    border-radius: 40px;
    background: linear-gradient(160deg, var(--photo-mid) 0%, var(--photo-dark) 70%);
    opacity: 0.85;
  }
  .tyre-track {
    position: absolute;
    left: 0;
    top: 880px;
    width: 600px;
    height: 320px;
  }
  .showtimes__board {
    position: absolute;
    left: 69px;
    top: 985px;
    width: 448px;
    height: 215px;
    background: var(--white);
  }
  .showtimes__label {
    position: absolute;
    left: 600px;
    top: 905px;
    font-size: 64px;
    font-weight: 800;
    font-style: italic;
    color: var(--white);
    line-height: 0.95;
    transform: rotate(-18deg);
    transform-origin: left top;
    text-align: left;
  }
  .showtimes__label span { display: block; }
  .showtimes__label span + span { margin-left: 10px; }
</style>
</head>
<body>
  <main class="poster">
    <div class="poster__backdrop" role="img" aria-label="Dark background with red and blue grunge brush-stroke textures"></div>

    <h1 class="headline">
      <span class="headline__discipline">MOUNTAIN BIKE</span>
      <span class="headline__trials">(TRIALS)</span>
      <span class="headline__show">STUNT SHOW</span>
    </h1>

    <div class="rider-photo" role="img" aria-label="Cut-out photo of the rider in a helmet performing a trials hop on a bike"></div>

    <svg class="tyre-track" viewBox="0 0 600 320" role="img" aria-label="White tyre track print sweeping across the bottom">
      <polygon points="0,150 560,40 600,120 560,320 0,320" fill="#ffffff" opacity="0.78"/>
    </svg>

    <section class="showtimes">
      <div class="showtimes__board"></div>
      <h2 class="showtimes__label"><span>SHOW</span><span>TIMES</span></h2>
    </section>
  </main>
</body>
</html>
```